Customer Dashboard Design for Email Security SaaS

Mailbrook is a commercial email spam filter offered as a SaaS product, built and operated by a small German hosting provider. It protects business email accounts against spam, phishing, scam, and viruses using a multilayer filtering pipeline that combines traditional spam detection with AI-powered classification. The product runs entirely on German infrastructure, ensuring data sovereignty for European customers.

We need a complete redesign of the customer-facing dashboard. This is the web application where paying customers manage their email filtering: view their mail log, check quarantined emails, manage allow/blocklists, configure their settings, and handle their subscription. It is the primary touchpoint between Mailbrook and its customers.

Our customers are system administrators, IT managers at small-to-medium businesses, and operators of small hosting providers. They are technically competent but not designers. They expect professional, efficient tools that respect their time. They typically manage 10–500 email accounts and check the dashboard a few times per week, with heavier use during spam incidents.

We have attached the current mockups which really need to be replaced with something good looking.

Target Market(s)

System administrators, IT managers at small-to-medium businesses, and operators of small hosting providers.

Industry/Entity Type

SaaS

Number of Pages Required

5+ page

```html
<!DOCTYPE html>
<html lang="de">
<head>
<meta charset="utf-8">
<title>Mailbrook – Übersicht</title>
<link href="https://fonts.googleapis.com/css2?family=Poppins:wght@400;500;600&family=Inter:wght@400;500;600&display=swap" rel="stylesheet">
<style>
:root{
  --bg:#171311;
  --panel:#1b1a19;
  --panel-border:#2a2826;
  --soft:#2a2a29;
  --text:#f2f2f2;
  --muted:#a9a9a9;
  --dim:#6f6f6f;
  --green:#0f9c6c;
  --green-dark:#0b4a3a;
  --red:#f0463c;
  --orange:#f07a2a;
  --blue:#4a6cf0;
  --yellow:#c9b41a;
  --grey:#8a8a8a;
}
*{box-sizing:border-box;margin:0;padding:0}
html,body{width:1200px;height:904px;overflow:hidden}
body{
  position:relative;
  font-family:"Poppins",sans-serif;
  color:var(--text);
  background:
    radial-gradient(ellipse 500px 300px at 620px 140px,rgba(70,45,20,.35),transparent 70%),
    radial-gradient(ellipse 600px 400px at 1150px 880px,rgba(60,35,20,.35),transparent 70%),
    var(--bg);
}
.abs{position:absolute}
.box{background:var(--panel);border:1px solid var(--panel-border);border-radius:6px}

/* sidebar */
.sidebar{left:15px;top:15px;width:232px;height:848px}
.brand-mark{left:34px;top:38px;width:37px;height:37px;border-radius:9px;background:var(--green)}
.brand-name{left:81px;top:44px;font-size:19px;font-weight:500}
.collapse{left:209px;top:45px}
.nav-line{left:34px;top:127px;width:1px;height:318px;background:#3a3836}
.nav-active{left:45px;top:108px;width:170px;height:37px;border-radius:6px;background:#2b2b2a;border-top:1px solid #1f5a46}
.nav-item{left:58px;height:20px;display:flex;align-items:center;gap:14px;font-size:12px;color:var(--muted)}
.nav-item.active{color:var(--text)}
.nav-item::before{content:"";position:absolute;left:-23px;top:10px;width:10px;height:1px;background:#3a3836}
.nav-item svg{width:18px;height:18px}
.side-divider{left:40px;width:183px;height:1px;background:#333}
.avatar{border-radius:50%;background:linear-gradient(160deg,#9a8a7a,#4a3e36)}
.side-user{left:90px;top:706px;font-size:11.5px;font-weight:600}
.mode-btn{left:41px;top:758px;width:31px;height:31px;border-radius:50%;background:#111;border:1px solid #333}
.mode-label{left:90px;top:765px;font-size:11.5px;font-weight:600}
.toggle{left:172px;top:758px;width:50px;height:30px;border-radius:15px;border:1px solid #3a3a3a;background:#141414}
.toggle::after{content:"";position:absolute;left:7px;top:5px;width:20px;height:20px;border-radius:50%;background:#0e4a3c}
.logout{left:34px;top:803px;width:190px;height:38px;border-radius:6px;background:#262625;display:flex;align-items:center;padding:0 14px;gap:12px;font-size:12px}
.logout .chev{margin-left:auto}

/* top bar */
.topbar{left:278px;top:14px;width:887px;height:53px}
.search{left:292px;top:24px;width:355px;height:32px;border-radius:16px;background:#121212;border:1px solid #2a2a2a;font-family:"Inter",sans-serif;font-size:10px;padding:9px 14px;color:#ddd}
.search-btn{left:616px;top:26px;width:28px;height:28px;border-radius:50%;background:var(--green);display:flex;align-items:center;justify-content:center}
.icon-btn{top:24px;width:31px;height:31px;border-radius:50%;border:1px solid #444;background:#1f1f1f;display:flex;align-items:center;justify-content:center}
.role{left:1077px;top:26px;font-family:"Inter",sans-serif;font-size:10px;font-weight:500;line-height:14px}
.role b{font-size:11px;font-weight:600;display:block}

/* greeting */
.title{left:277px;top:99px;font-size:25px;font-weight:600}
.subtitle{left:277px;top:136px;font-size:14px}

/* stats */
.stat{top:195px;width:282px;height:119px}
.stat .pill{position:absolute;left:21px;top:21px;height:34px;padding:0 14px;border-radius:4px;background:#2c2c2b;font-size:15px;display:flex;align-items:center;letter-spacing:.3px}
.stat .num{position:absolute;left:22px;top:64px;font-size:36px;font-weight:600;line-height:1}
.stat .note{position:absolute;top:70px;font-family:"Inter",sans-serif;font-size:10.5px;line-height:15px;color:#e6e6e6}
.stat .ico{position:absolute;right:20px;top:20px}

/* chart */
.chart{left:277px;top:371px;width:889px;height:493px}
.chart h2{position:absolute;left:22px;top:20px;font-size:23px;font-weight:600}
.filter{top:434px;height:27px;border-radius:3px;background:#1e1e1e;font-family:"Inter",sans-serif;font-size:11px;display:flex;align-items:center;justify-content:center;border:1px solid #333}
.f-all{border-color:#1d4a3c;color:#fff}
.f-spam{color:var(--red);border-color:#4a1e1a}
.f-phish{color:var(--orange);border-color:#4a2c18}
.f-virus{color:var(--red);border-color:#4a1e1a}
.f-news{color:var(--blue);border-color:#2a3a9a;background:#1a1d2e}
.range{top:435px;width:66px;height:27px;border-radius:4px;background:#2c2c2b;font-family:"Inter",sans-serif;font-size:12px;display:flex;align-items:center;justify-content:center;font-weight:500}
.range.on{border-top:1px solid #1f5a46}
.chart svg.plot{position:absolute;left:0;top:0}
.legend{left:297px;top:772px;display:flex;gap:28px;font-family:"Inter",sans-serif;font-size:12px;font-weight:500}
.legend span{display:flex;align-items:center;gap:7px}
.legend i{width:10px;height:10px;border-radius:1px;display:block}
.data-link{left:297px;top:808px;font-family:"Inter",sans-serif;font-size:14px}
</style>
</head>
<body>

<!-- Sidebar -->
<aside class="abs box sidebar"></aside>
<div class="abs brand-mark"></div>
<div class="abs brand-name">Mailbrook</div>
<svg class="abs collapse" width="22" height="22" viewBox="0 0 22 22" fill="none" stroke="#ddd" stroke-width="1.3"><rect x="1" y="1" width="20" height="20" rx="2"/><line x1="7" y1="1" x2="7" y2="21"/><polyline points="14,8 11,11 14,14"/></svg>

<div class="abs nav-line"></div>
<div class="abs nav-active"></div>
<nav>
  <div class="abs nav-item active" style="top:117px"><svg viewBox="0 0 18 18" fill="none" stroke="#fff" stroke-width="1.3"><path d="M3 8l6-5 6 5v8H11v-5H7v5H3z"/></svg>Übersicht</div>
  <div class="abs nav-item" style="top:160px"><svg viewBox="0 0 18 18" fill="none" stroke="#ddd" stroke-width="1.3"><path d="M2 4h14M2 7h14M2 10h14M2 13h14"/></svg>Mail-Log</div>
  <div class="abs nav-item" style="top:204px"><svg viewBox="0 0 18 18" fill="none" stroke="#ddd" stroke-width="1.3"><path d="M2 7l7-4 7 4v8H2z"/><path d="M2 7l7 4 7-4"/></svg>Postfächer</div>
  <div class="abs nav-item" style="top:250px"><svg viewBox="0 0 18 18" fill="none" stroke="#ddd" stroke-width="1.3"><circle cx="6" cy="7" r="3"/><path d="M1 15c0-3 2-4 5-4s5 1 5 4M12 6h5M12 9h5M12 12h5"/></svg>Allowlist</div>
  <div class="abs nav-item" style="top:295px"><svg viewBox="0 0 18 18" fill="none" stroke="#ddd" stroke-width="1.3"><circle cx="7" cy="6" r="3"/><path d="M1 16c0-3 2-5 6-5"/><circle cx="13" cy="13" r="3"/><line x1="11" y1="15" x2="15" y2="11"/></svg>Blocklist</div>
  <div class="abs nav-item" style="top:342px"><svg viewBox="0 0 18 18" fill="none" stroke="#ddd" stroke-width="1.3"><rect x="3" y="8" width="12" height="8" rx="1"/><path d="M6 8V5a3 3 0 016 0v3"/></svg>Quarantane</div>
  <div class="abs nav-item" style="top:389px"><svg viewBox="0 0 18 18" fill="none" stroke="#ddd" stroke-width="1.3"><circle cx="9" cy="9" r="2.5"/><path d="M9 2l1.5 2 2.5-.5.5 2.5 2 1.5-1 2 1 2-2 1.5-.5 2.5-2.5-.5L9 16l-1.5-2-2.5.5-.5-2.5-2-1.5 1-2-1-2 2-1.5.5-2.5 2.5.5z"/></svg>Einstellungen</div>
  <div class="abs nav-item" style="top:435px"><svg viewBox="0 0 18 18" fill="none" stroke="#ddd" stroke-width="1.3"><rect x="2" y="3" width="14" height="10" rx="1"/><path d="M6 16h6M9 13v3"/><text x="9" y="11" font-size="7" text-anchor="middle" fill="#ddd" stroke="none">$</text></svg>Abrechnung</div>
</nav>

<div class="abs side-divider" style="top:687px;left:15px;width:232px;background:#2c2c2c"></div>
<div class="abs avatar" role="img" aria-label="Profilfoto des Nutzers" style="left:41px;top:698px;width:31px;height:31px"></div>
<div class="abs side-user">Jonas Weber</div>
<svg class="abs" style="left:203px;top:706px" width="16" height="16" viewBox="0 0 16 16"><path d="M11 1a7 7 0 104 11A6 6 0 0111 1z" fill="#fff"/></svg>
<div class="abs side-divider" style="top:745px"></div>
<div class="abs mode-btn"><svg width="31" height="31" viewBox="0 0 31 31"><path d="M18 8a8 8 0 104 13 7 7 0 01-4-13z" fill="#fff"/></svg></div>
<div class="abs mode-label">Dark mode</div>
<div class="abs toggle"></div>
<div class="abs logout">
  <svg width="14" height="14" viewBox="0 0 14 14" fill="none" stroke="#fff" stroke-width="1.2"><path d="M5 1H1v12h4M5 7h8M10 4l3 3-3 3"/></svg>
  Logout
  <svg class="chev" width="10" height="10" viewBox="0 0 10 10" fill="none" stroke="#fff" stroke-width="1.2"><polyline points="2,4 5,7 8,4"/></svg>
</div>

<!-- Top bar -->
<header class="abs box topbar"></header>
<div class="abs search">Search...</div>
<div class="abs search-btn"><svg width="14" height="14" viewBox="0 0 14 14" fill="none" stroke="#fff" stroke-width="1.8"><circle cx="6" cy="6" r="4.3"/><line x1="9.2" y1="9.2" x2="13" y2="13"/></svg></div>
<div class="abs icon-btn" style="left:949px"><svg width="14" height="14" viewBox="0 0 14 14" fill="none" stroke="#fff" stroke-width="1.2"><path d="M1 6l6-4 6 4v7H1z"/><path d="M1 6l6 4 6-4"/></svg></div>
<div class="abs icon-btn" style="left:990px"><svg width="14" height="14" viewBox="0 0 14 14" fill="none" stroke="#fff" stroke-width="1.2"><path d="M3 10V6a4 4 0 018 0v4l1 1H2z"/><path d="M6 12.5h2"/></svg></div>
<div class="abs avatar" role="img" aria-label="Profilfoto des Administrators" style="left:1036px;top:24px;width:31px;height:31px"></div>
<div class="abs role">Super Admin<b>Jonas Weber</b></div>

<!-- Greeting -->
<h1 class="abs title">Guten Tag</h1>
<p class="abs subtitle">Seobachtungsmodus - Mails Werden Analysiert Aber Nicht Blockiert</p>

<!-- Stats -->
<section class="abs box stat" style="left:277px">
  <div class="pill">Letzte 24&nbsp;&nbsp;Stunden</div>
  <svg class="ico" width="36" height="36" viewBox="0 0 36 36" fill="none" stroke="#fff" stroke-width="1.5"><circle cx="18" cy="18" r="16.5"/><path d="M18 9v9l-4 4"/></svg>
  <div class="num">85</div>
  <div class="note" style="left:76px">O zugestellt,<br>O abgefangen</div>
</section>
<section class="abs box stat" style="left:581px">
  <div class="pill">7 TAGE</div>
  <svg class="ico" width="34" height="34" viewBox="0 0 34 34" fill="none" stroke="#fff" stroke-width="1.5"><path d="M4 6l10-3 17 17-11 11L3 14z"/><circle cx="11" cy="10" r="2.5"/><path d="M16 24l8-8"/></svg>
  <div class="num">34</div>
  <div class="note" style="left:82px">0%<br>zugestellt</div>
</section>
<section class="abs box stat" style="left:884px">
  <div class="pill">30 TAGE</div>
  <svg class="ico" width="32" height="34" viewBox="0 0 32 34" fill="none" stroke="#fff" stroke-width="1.5"><rect x="1" y="5" width="26" height="24" rx="3"/><path d="M1 12h26M8 1v7M20 1v7"/><circle cx="24" cy="26" r="6" fill="#1b1a19"/><path d="M24 23v3l2 1.5"/></svg>
  <div class="num">42</div>
  <div class="note" style="left:82px">0%<br>0% zugestellt</div>
</section>

<!-- Chart panel -->
<section class="abs box chart">
  <h2>Letzte 30 Tage</h2>
  <svg class="plot" width="889" height="493" viewBox="0 0 889 493" font-family="Inter, sans-serif">
    <defs>
      <linearGradient id="barGreen" x1="0" y1="0" x2="0" y2="1">
        <stop offset="0" stop-color="#e6f7f0"/>
        <stop offset=".35" stop-color="#0f9c6c"/>
        <stop offset="1" stop-color="#0f9c6c" stop-opacity="0"/>
      </linearGradient>
      <linearGradient id="barGrey" x1="0" y1="0" x2="0" y2="1">
        <stop offset="0" stop-color="#333"/>
        <stop offset="1" stop-color="#1d1d1d" stop-opacity=".4"/>
      </linearGradient>
    </defs>
    <line x1="22" y1="167" x2="864" y2="167" stroke="#2e2e2e"/>
    <line x1="22" y1="267" x2="864" y2="267" stroke="#2a2a2a"/>
    <rect x="22"  y="194" width="110" height="149" rx="4" fill="url(#barGreen)"/>
    <rect x="143" y="240" width="110" height="103" rx="4" fill="url(#barGrey)"/>
    <rect x="264" y="248" width="110" height="95"  rx="4" fill="url(#barGrey)"/>
    <rect x="385" y="256" width="110" height="87"  rx="4" fill="url(#barGrey)"/>
    <rect x="506" y="215" width="110" height="128" rx="4" fill="url(#barGreen)"/>
    <rect x="627" y="192" width="110" height="151" rx="4" fill="url(#barGrey)"/>
    <rect x="748" y="152" width="110" height="191" rx="4" fill="url(#barGreen)"/>
    <line x1="22" y1="378" x2="864" y2="378" stroke="#2e2e2e"/>
    <g fill="#6f6f6f" font-size="12" text-anchor="middle">
      <text x="77" y="361">4/8</text><text x="198" y="361">4/9</text><text x="319" y="361">4/10</text>
      <text x="440" y="361">4/11</text><text x="561" y="361">4/12</text><text x="682" y="361">4/13</text><text x="803" y="361">4/14</text>
    </g>
    <g fill="#fff" font-size="12" text-anchor="middle">
      <rect x="55" y="155" width="44" height="26" rx="4" fill="#2c2c2b"/><text x="77" y="172">4/8</text>
      <line x1="79" y1="181" x2="79" y2="194" stroke="#fff"/><circle cx="79" cy="194" r="5.5"/>
      <rect x="536" y="174" width="46" height="26" rx="4" fill="#2c2c2b"/><text x="559" y="191">4/12</text>
      <line x1="559" y1="200" x2="559" y2="215" stroke="#fff"/><circle cx="559" cy="215" r="5.5"/>
      <rect x="780" y="110" width="46" height="26" rx="4" fill="#2c2c2b"/><text x="803" y="127">4/14</text>
      <line x1="803" y1="136" x2="803" y2="150" stroke="#fff"/><circle cx="803" cy="150" r="5.5"/>
    </g>
  </svg>
</section>

<div class="abs filter f-all" style="left:299px;width:80px">ALLE</div>
<div class="abs filter f-spam" style="left:387px;width:80px">SPAM</div>
<div class="abs filter f-phish" style="left:474px;width:95px">PHISHING</div>
<div class="abs filter f-virus" style="left:576px;width:75px">VIRUS</div>
<div class="abs filter f-news" style="left:658px;width:110px">NEWSLETTER</div>

<div class="abs range on" style="left:921px">7 TAGE</div>
<div class="abs range" style="left:996px">14 TAGE</div>
<div class="abs range" style="left:1070px">30 TAGE</div>

<div class="abs legend">
  <span><i style="background:var(--green)"></i>AKZEPTIERT</span>
  <span><i style="background:var(--red)"></i>ABGELEHNT</span>
  <span><i style="background:var(--yellow)"></i>QUARANTÄNE</span>
  <span><i style="background:var(--grey)"></i>TEMPFAIL</span>
</div>
<div class="abs data-link">Datentabelle Anzeigen</div>

</body>
</html>
```